I want a brand new webshop for my automotive company Quenthor

<br/>I would like to have a webshop for the products that I now sell.<br/><br/>What is important is that it is a well-organized website and that I can make adjustments to it myself.<br/><br/>I have added more information in the document and explained everything in steps what I want. I also added an example website so that you can see a little bit what we like<br/>

Target Market(s)

automotive Branche

Industry/Entity Type

Automotive

Coding

Coded - Design and coding required

Number of Pages Required

5+ page

Font styles to use
Sans Serif

Colors

Designer to choose colors to be used in the design.

Requirements
Must have
• things that should be on the website:
• he points websites:
• - Possibility of choosing different languages
• - Newsletter subscription
• - Dropdown under categories
• - The search menu: "I am looking for"
• - Products on the home page alike (in our case think different categories)
• - Well-arranged menu on the side with which they go to the different categories
• - Mobile responsive
• - Shopping basket at the top of the header
• - State social media channels on the website
• - Coockie popup bar
• - Benefits on the page
• - All photos with a white background, are beautiful and well-arranged
• - Reviews from people who have already purchased products from us
• - Chat Function on the website ?? People can ask questions here
• - Can order on the product page and on the overview page Check example: https://www.werkmaxo.nl/automotive-gereedschappen/koelsysteem-verwarming-en-airconditioning
• - Ratewharf or something in that trend needs to be added
• - Footer cups: frequently asked questions, privacy, general terms and conditions, returns and warranty, shipping etc etc
• - Check account content (mandelpijp.nl) (confirmation email)
• - About us"
• - Cup with Video?
• - We send with (pormindo site at the bottom)
• - Related products at every product page
• - Last viewed (DKT)
• - Photo of someone on the website
• - Pop up (business / private) so you don't have to log in and you keep it easier. Check: https://www.lindevoort.nl/
• - Chamber of Commerce and VAT number of course
• - Link to the catalog (so that they can download it)
• - Featured or Most sold collection above
• - and of course pages for different collections

```html
<!DOCTYPE html>
<html lang="en">
<head>
<meta charset="utf-8">
<title>Quenthor Tools Store</title>
<link href="https://fonts.googleapis.com/css2?family=Montserrat:wght@400;500;600;700;800;900&family=Quicksand:wght@400;500;600;700&display=swap" rel="stylesheet">
<style>
:root{
  --navy-deep:#0f1c3c;
  --navy:#22278c;
  --gold:#e2b52b;
  --gold-soft:#e8c24a;
  --red:#e0261e;
  --ink:#222634;
  --muted:#8a8a8a;
  --line:#e2e2e2;
  --page:#efefef;
  --foot:#121212;
  --foot-strip:#2e2e2e;
  --tick:#3bb54a;
}
*{box-sizing:border-box;margin:0;padding:0}
html,body{width:1200px;height:2952px;overflow:hidden}
body{font-family:"Quicksand",sans-serif;color:var(--ink);background:var(--page)}
.page{position:relative;width:1200px;height:2952px;overflow:hidden;background:var(--page)}
.abs{position:absolute}
a{color:inherit;text-decoration:none}
.mont{font-family:"Montserrat",sans-serif}

.masthead{left:0;top:0;width:1200px;height:119px;background:var(--navy-deep)}
.topbar-text{top:13px;font-size:12px;color:#c9cde0;font-weight:600}
.brand{display:flex;align-items:center;gap:10px}
.brand-square{width:40px;height:40px;background:var(--gold)}
.brand-name{font-family:"Montserrat",sans-serif;font-weight:700;color:var(--gold);font-size:30px;letter-spacing:.5px}
.search{left:333px;top:58px;width:521px;height:42px;border-radius:21px;background:#e9e9ee;display:flex;align-items:center;padding-left:20px;font-size:12px;color:#8a8ea0}
.search-btn{right:6px;top:6px;width:30px;height:30px;border-radius:50%;background:var(--gold)}
.account{font-size:12px;color:#aab0c8;line-height:19px}

.navband{left:0;top:119px;width:1200px;height:48px;background:var(--gold)}
.cat-head{left:61px;top:119px;width:247px;height:48px;background:var(--red);color:#fff;font-family:"Montserrat",sans-serif;font-weight:700;font-size:13px;display:flex;align-items:center;gap:8px;padding-left:14px}
.nav-item{top:143px;font-family:"Montserrat",sans-serif;font-weight:600;font-size:11.5px;color:var(--navy-deep);letter-spacing:.3px}
.nav-active{left:319px;top:137px;width:57px;height:30px;background:var(--navy-deep);border-radius:7px 7px 0 0;color:#fff;font-family:"Montserrat",sans-serif;font-weight:600;font-size:11.5px;display:flex;align-items:center;justify-content:center}
.offer{left:981px;top:128px;width:146px;height:35px;border:1.5px solid #333;background:#f4e4b4;display:flex;align-items:center;justify-content:center;gap:5px;font-family:"Montserrat",sans-serif;font-weight:700;font-size:13px;color:var(--navy-deep)}
.offer b{color:var(--red);font-size:20px;font-weight:800}

.hero-left{left:0;top:167px;width:61px;height:423px;background:var(--navy-deep)}
.cat-list{left:61px;top:167px;width:247px;height:423px;background:var(--gold-soft);list-style:none;padding:6px 14px 0}
.cat-list li{height:37.6px;display:flex;align-items:center;justify-content:space-between;font-size:12px;font-weight:600;color:#2a2f6e;border-bottom:1px solid rgba(255,255,255,.35)}
.cat-list li:last-child{border-bottom:none}
.hero-photo{left:308px;top:167px;width:892px;height:423px;background:linear-gradient(180deg,#d7d2c8 0%,#b9ad95 35%,#8d7d5d 60%,#55503f 85%,#2e2d2a 100%)}
.hero-h{font-family:"Montserrat",sans-serif;font-weight:900;text-align:right;right:39px;line-height:1;white-space:nowrap}
.hero-1{top:180px;font-size:46px;color:var(--navy-deep)}
.hero-2{top:227px;font-size:37px;color:var(--red)}
.hero-3{top:270px;font-size:26px;color:#dcdcea;font-weight:800}
.hero-band{left:856px;top:302px;width:310px;height:28px;background:#3a2d8c;color:#fff;font-family:"Montserrat",sans-serif;font-weight:600;font-size:18.5px;display:flex;align-items:center;justify-content:center;white-space:nowrap}
.explore{left:1054px;top:517px;width:107px;height:27px;background:var(--red);color:#fff;font-weight:700;font-size:13px;display:flex;align-items:center;justify-content:center}

.auth{left:350px;top:197px;width:499px;height:326px;background:#fff;box-shadow:0 4px 18px rgba(0,0,0,.3)}
.auth-head{height:36px;background:#1b1d2e;color:#fff;font-family:"Montserrat",sans-serif;font-weight:600;font-size:12.5px;display:flex;align-items:center;gap:8px;padding-left:18px}
.field{left:17px;width:206px;height:32px;border:1px solid #d8d8d8;display:flex;align-items:center;font-size:12px;color:#555;background:#f6f6f6}
.field i{width:34px;height:100%;background:#b8b8b8;margin-right:10px;display:block}
.auth small{font-size:12px;color:#333;font-weight:600}
.social{top:186px;width:34px;height:28px}
.btn-login{left:17px;top:256px;width:87px;height:36px;background:var(--navy);color:#fff;font-family:"Montserrat",sans-serif;font-weight:600;font-size:13px;display:flex;align-items:center;justify-content:center}
.auth-divider{left:249px;top:24px;width:1px;height:254px;background:#e4e4e4}
.auth-right li{list-style:none;font-size:11px;color:#333;margin-bottom:11px;font-weight:600}
.btn-create{left:280px;top:189px;width:174px;height:37px;background:var(--gold);color:#fff;font-family:"Montserrat",sans-serif;font-weight:600;font-size:12.5px;display:flex;align-items:center;justify-content:center}

.sec-title{font-family:"Montserrat",sans-serif;font-weight:500;font-size:16.5px;color:#2a2d40;display:flex;align-items:center;gap:6px;letter-spacing:.2px}
.sec-count{font-size:11.5px;color:#555;font-weight:600}
.sec-count span{color:var(--navy)}

.product-card{width:167px;height:314px;background:#fff;border:1px solid var(--line);text-align:center}
.product-shot{width:110px;height:160px;margin:10px auto 0;background:linear-gradient(180deg,#d94040 0%,#7b7b7b 30%,#c9c14a 60%,#909090 100%);border-radius:6px;opacity:.85}
.shot-bottle{background:linear-gradient(180deg,#e9e9e9 0%,#e7dc3a 35%,#d8c22a 90%)}
.shot-case{height:120px;margin-top:30px;background:linear-gradient(180deg,#d33 0%,#3a3a3a 40%,#c8b43a 100%)}
.shot-slim{width:70px;background:linear-gradient(180deg,#d8c23a 0%,#8c8c8c 50%,#bdbdbd 100%)}
.product-name{font-family:"Montserrat",sans-serif;font-weight:500;font-size:16.5px;color:#2a2d40;margin-top:16px}
.product-desc{font-size:11px;line-height:14px;color:#777;margin:2px 10px 0;font-weight:500}
.btn-view{position:absolute;left:50%;bottom:14px;transform:translateX(-50%);width:76px;height:24px;background:var(--navy);color:#fff;font-size:12px;font-weight:600;display:flex;align-items:center;justify-content:center}
.arrow{width:24px;height:24px;border-radius:50%;background:#e6e6e6;display:flex;align-items:center;justify-content:center}

.mini-card{top:1567px;width:149px;height:192px;background:#fff;border:1px solid var(--line);text-align:center}
.mini-card.current{border-color:var(--gold)}
.mini-card h4{font-family:"Montserrat",sans-serif;font-weight:500;font-size:14px;margin-top:18px;color:#2a2d40}
.mini-shot{width:46px;height:90px;margin:8px auto 0;background:linear-gradient(180deg,#d33 0%,#555 40%,#c8b43a 100%);border-radius:4px}
.mini-card .btn-view{bottom:22px}

.hotdeals{left:69px;top:661px;width:226px;height:443px;background:#fff;border:1px solid #1d2380}
.hotdeals-head{height:38px;background:#1d2380;color:#fff;font-family:"Montserrat",sans-serif;font-weight:700;font-size:13px;display:flex;align-items:center;justify-content:space-between;padding:0 8px 0 20px}
.dot-arrow{width:22px;height:22px;border-radius:50%;background:#5a5e9a;display:inline-block;margin-left:4px}
.count-cell{top:366px;width:49px;height:41px;border-right:1px solid #ddd;text-align:center}
.count-cell b{display:block;font-family:"Montserrat",sans-serif;font-size:14px;margin-top:5px}
.count-cell span{font-size:7px;color:#888;font-weight:700}
.promo{left:63px;top:1146px;width:237px;height:293px;background:linear-gradient(135deg,#c9a630 0%,#c9a630 35%,#4a4a4a 60%,#8a2020 80%,#2b2b2b 100%);border-radius:4px}
.testimonials{left:69px;top:1490px;width:226px;height:252px;border:1px solid #e4e4e4;background:#f4f4f4}
.callus{left:71px;top:1750px;width:224px;height:84px;background:linear-gradient(90deg,#3a3a3a,#1d1d1d)}
.perk{left:86px;display:flex;gap:10px;align-items:flex-start}
.perk i{width:26px;height:26px;display:block}
.perk b{font-family:"Montserrat",sans-serif;font-size:11px;font-weight:700;color:#1b1d2e}
.perk p{font-size:10px;color:#888;font-weight:600;margin-top:2px}
.rating{left:69px;top:2066px;width:226px;height:206px;border:1px solid #e4e4e4;background:#fafafa;text-align:center}

.benefit-icon{left:357px;width:64px;height:64px;border-radius:50%;border:2px solid #e1e1e1;color:#d1d1d1;font-family:"Montserrat",sans-serif;font-weight:700;display:flex;align-items:center;justify-content:center;font-size:14px}
.benefit-title{left:435px;font-family:"Montserrat",sans-serif;font-weight:700;font-size:11px;color:#2a2d40}
.benefit-text{left:435px;width:345px;font-size:12px;line-height:15px;color:#777;font-weight:500}
.brand-cell{top:2169px;height:103px;background:#fff;border-right:1px solid #eee;display:flex;align-items:center;justify-content:center;font-family:"Montserrat",sans-serif;font-weight:700;font-size:18px;letter-spacing:1px;color:#444}

.news{left:0;top:2306px;width:1200px;height:83px;background:var(--foot-strip)}
.sq{top:2331px;width:32px;height:32px;border:1px solid #666;background:#3a3a3a}
.footer{left:0;top:2389px;width:1200px;height:499px;background:var(--foot)}
.feat-title{font-size:14.5px;color:#d6d6d6;font-weight:600}
.feat-sub{font-size:10px;color:#8a8a8a;font-weight:700;font-style:italic;width:170px;line-height:13px}
.ticks{list-style:none}
.ticks li{font-size:11px;color:#cfcfcf;font-weight:700;margin-bottom:7px;display:flex;gap:6px;align-items:center}
.ticks li::before{content:"";width:8px;height:5px;border-left:2px solid var(--tick);border-bottom:2px solid var(--tick);transform:rotate(-45deg);margin-top:-3px}
.foot-h{font-size:14px;color:#c8c8c8;font-weight:600}
.foot-text{font-size:12px;line-height:17.5px;color:#7a7a7a;font-weight:500}
.foot-links{list-style:none}
.foot-links li{font-size:10.5px;color:#555;margin-bottom:10px;font-weight:600}
.pay{top:2848px;width:36px;height:21px;border-radius:3px}
.copyright{left:0;top:2888px;width:1200px;height:28px;background:var(--gold);display:flex;align-items:center;justify-content:center;font-size:10px;color:#3a2d00;font-weight:600}
.cookie{left:0;top:2916px;width:1200px;height:36px;background:#f0f0f0;display:flex;align-items:center;padding-left:332px;gap:14px;font-size:9.5px;color:#444;font-weight:600}
.cookie-btn{border:1px solid #999;padding:5px 6px;font-size:9px}
</style>
</head>
<body>
<div class="page">

  <header class="abs masthead">
    <p class="abs topbar-text" style="left:60px">Welcome to Quenthor Tools Store</p>
    <p class="abs topbar-text" style="left:945px">Wishlist (0)</p>
    <p class="abs topbar-text" style="left:1032px">USD</p>
    <p class="abs topbar-text" style="left:1083px">English</p>
    <a class="abs brand" style="left:63px;top:55px"><span class="brand-square"></span><span class="brand-name">QUENTHOR</span></a>
    <div class="abs search">I am looking for...
      <span class="abs search-btn"><svg width="30" height="30" viewBox="0 0 30 30"><circle cx="14" cy="14" r="5" fill="none" stroke="#7a5a00" stroke-width="1.6"/><line x1="18" y1="18" x2="21" y2="21" stroke="#7a5a00" stroke-width="1.6"/></svg></span>
    </div>
    <svg class="abs" style="left:917px;top:60px" width="20" height="20" viewBox="0 0 20 20"><circle cx="10" cy="6" r="4" fill="none" stroke="#aab0c8" stroke-width="1.4"/><path d="M2 19c1-5 5-7 8-7s7 2 8 7" fill="none" stroke="#aab0c8" stroke-width="1.4"/></svg>
    <div class="abs account" style="left:917px;top:62px"><span style="margin-left:24px">Sign In</span><br>My Account &nbsp;▾</div>
    <svg class="abs" style="left:1031px;top:56px" width="34" height="36" viewBox="0 0 34 36"><path d="M2 6h5l4 18h17l3-12H9" fill="none" stroke="#aab0c8" stroke-width="1.6"/><circle cx="13" cy="30" r="2.5" fill="none" stroke="#aab0c8" stroke-width="1.4"/><circle cx="26" cy="30" r="2.5" fill="none" stroke="#aab0c8" stroke-width="1.4"/><path d="M15 14l3 3 6-7" fill="none" stroke="#3bb54a" stroke-width="1.6"/></svg>
    <div class="abs account" style="left:1069px;top:60px">My Cart<br><span style="color:var(--gold)">$0.00</span></div>
  </header>

  <nav class="abs navband" aria-label="Main"></nav>
  <div class="abs cat-head">
    <svg width="22" height="12" viewBox="0 0 22 12"><path d="M4 0h3L3 12H0zM10 0h3L9 12H6zM16 0h3l-4 12h-3z" fill="#fff"/></svg>TOP CATEGORIES
  </div>
  <a class="abs nav-active">HOME</a>
  <a class="abs nav-item" style="left:393px">PRODUCTEN</a>
  <a class="abs nav-item" style="left:496px">REGISTER</a>
  <a class="abs nav-item" style="left:582px">SERVICE</a>
  <a class="abs nav-item" style="left:661px">WAAR TE KOOP</a>
  <a class="abs nav-item" style="left:780px">VIDEO</a>
  <a class="abs nav-item" style="left:846px">CONTACT US</a>
  <div class="abs offer">Get <b>40%</b> Offer</div>

  <div class="abs hero-left"></div>
  <ul class="abs cat-list">
    <li>Gloeibougies Verwijderen</li>
    <li>Verstuivertrekkers</li>
    <li>Neusbreuksets verstuivers</li>
    <li>Brandplaat Verwijdern</li>
    <li>Uitbreingen</li>
    <li>Schoonmaak- en schuursets</li>
    <li>Quenthor Hydrauliek</li>
    <li>Overige accesoires</li>
    <li>Reparatiesets / algemeen</li>
    <li>Montageset / accessoires</li>
    <li>More Categories <span style="font-size:16px">+</span></li>
  </ul>
  <div class="abs hero-photo" role="img" aria-label="White service van driving on a country road"></div>
  <p class="abs hero-h hero-1">INOOVATIVE</p>
  <p class="abs hero-h hero-2">AUTOMOTIVE</p>
  <p class="abs hero-h hero-3">QUENTHOR SERVICE</p>
  <p class="abs hero-band">THINKING NEW POSSIBILITIES</p>
  <a class="abs explore">Explore now</a>

  <section class="abs auth" aria-label="Sign in or register">
    <div class="auth-head">
      <svg width="16" height="16" viewBox="0 0 20 20"><circle cx="10" cy="6" r="4" fill="none" stroke="#fff" stroke-width="1.6"/><path d="M2 19c1-5 5-7 8-7s7 2 8 7" fill="none" stroke="#fff" stroke-width="1.6"/></svg>SIGN IN / REGISTER
    </div>
    <div class="abs field" style="top:70px"><i></i>E-mail Address</div>
    <div class="abs field" style="top:115px"><i></i>Password</div>
    <small class="abs" style="left:17px;top:165px">Login with your social account</small>
    <span class="abs social" style="left:17px;background:#dd4b39" aria-label="Social sign in 1"></span>
    <span class="abs social" style="left:53px;background:#3b5a9a" aria-label="Social sign in 2"></span>
    <span class="abs social" style="left:89px;background:#3aa8e0" aria-label="Social sign in 3"></span>
    <span class="abs social" style="left:125px;background:#1a6fa8" aria-label="Social sign in 4"></span>
    <small class="abs" style="left:17px;top:226px;font-weight:500">Forgot Your Password? <u>click here</u></small>
    <a class="abs btn-login">LOGIN</a>
    <span class="abs auth-divider"></span>
    <div class="abs auth-right" style="left:283px;top:68px">
      <p class="mont" style="color:var(--navy);font-weight:600;font-size:13px">NEW HERE?</p>
      <p style="font-size:12px;font-weight:700;margin:3px 0 12px">Registration is free and easy!</p>
      <ul><li>• Faster checkout</li><li>• Save multiple shipping addresses</li><li>• View and track orders and more</li></ul>
    </div>
    <a class="abs btn-create">CREATE AN ACCOUNT</a>
  </section>

  <svg class="abs" style="left:0;top:590px" width="1200" height="40" viewBox="0 0 1200 40" preserveAspectRatio="none">
    <path d="M0 0H1200V6L1185 30 1170 6 1155 30 1140 6 1125 30 1110 6 1095 30 1080 6 1065 30 1050 6 1035 30 1020 6 1005 30 990 6 975 30 960 6 945 30 930 6 915 30 900 6 885 30 870 6 855 30 840 6 825 30 810 6 795 30 780 6 765 30 750 6 735 30 720 6 705 30 690 6 675 30 660 6 645 30 630 6 615 30 600 6 585 30 570 6 555 30 540 6 525 30 510 6 495 30 480 6 465 30 450 6 435 30 420 6 405 30 390 6 375 30 360 6 345 30 330 6 315 30 300 6 285 30 270 6 255 30 240 6 225 30 210 6 195 30 180 6 165 30 150 6 135 30 120 6 105 30 90 6 75 30 60 6 45 30 30 6 15 30 0 6Z" fill="#e8d28a"/>
  </svg>

  <aside class="abs hotdeals">
    <div class="hotdeals-head">HOT DEALS<span><span class="dot-arrow"></span><span class="dot-arrow"></span></span></div>
    <span class="abs" style="left:15px;top:55px;width:48px;height:21px;background:var(--gold);color:#fff;font-size:11px;font-weight:700;display:flex;align-items:center;justify-content:center;border-radius:3px">-14%</span>
    <div class="abs" role="img" aria-label="Injector puller tool" style="left:68px;top:64px;width:90px;height:232px;background:linear-gradient(180deg,#cc3434 0%,#d04040 25%,#7a7a7a 45%,#c7c04a 65%,#a0a0a0 100%);border-radius:8px;opacity:.85"></div>
    <p class="abs" style="left:0;width:226px;top:306px;text-align:center;font-size:12px;font-weight:600;color:#333">QTP110 &nbsp;Verstuiver-trekker</p>
    <p class="abs" style="left:0;width:226px;top:328px;text-align:center;font-size:12px;font-weight:700;color:var(--red)">$68.00 &nbsp;&nbsp;<s style="color:#999;font-weight:500">$79.00</s></p>
    <div class="abs" style="left:14px;top:366px;width:198px;height:43px;border:1px solid #ccc"></div>
    <div class="abs count-cell" style="left:15px"><b>317</b><span>DAYS</span></div>
    <div class="abs count-cell" style="left:64px"><b>01</b><span>HOURS</span></div>
    <div class="abs count-cell" style="left:113px"><b>36</b><span>MINS</span></div>
    <div class="abs count-cell" style="left:162px;border-right:none"><b>10</b><span>SECS</span></div>
  </aside>

  <div class="abs promo" role="img" aria-label="Korra power tool promotion, buying deal now, jigsaw on a workbench"></div>

  <section class="abs testimonials">
    <h3 class="abs mont" style="left:16px;top:14px;font-size:14px;font-weight:500;color:#444">Testimonials</h3>
    <div class="abs" role="img" aria-label="Customer portrait" style="left:17px;top:51px;width:74px;height:75px;background:linear-gradient(180deg,#d9d2c9,#8a6a55)"></div>
    <p class="abs" style="left:104px;top:60px;font-size:12.5px;font-weight:600;color:#555">Lena Vorst</p>
    <p class="abs" style="left:104px;top:77px;font-size:10.5px;font-weight:600;color:#999">Developer</p>
    <p class="abs" style="left:17px;top:145px;width:195px;font-size:11.5px;line-height:17px;color:#999;font-weight:500">Duis faucibus enim vitae nunc molestie, nec facilisis arcu pulvinar nullam mattis.</p>
    <svg class="abs" style="left:100px;top:219px" width="40" height="14" viewBox="0 0 40 14"><path d="M8 2 3 7l5 5M32 2l5 5-5 5" fill="none" stroke="#666" stroke-width="1.4"/></svg>
  </section>

  <div class="abs callus" role="img" aria-label="Hand holding a phone">
    <p class="abs" style="left:88px;top:30px;font-size:11px;color:#ddd;font-weight:600">Call Us Now:</p>
    <p class="abs mont" style="left:88px;top:45px;font-size:17px;color:#f05a28;font-weight:700;letter-spacing:.5px">0800-555-712</p>
  </div>

  <div class="abs perk" style="top:1858px"><i><svg width="26" height="22" viewBox="0 0 26 22"><path d="M1 3h14v12H1zM15 7h6l4 5v3h-10z" fill="none" stroke="#e0261e" stroke-width="1.5"/><circle cx="6" cy="17" r="2.5" fill="#fff" stroke="#e0261e" stroke-width="1.5"/><circle cx="20" cy="17" r="2.5" fill="#fff" stroke="#e0261e" stroke-width="1.5"/></svg></i><div><b>FREE SHIPPING</b><p>Free shipping on all UK oders</p></div></div>
  <div class="abs" style="left:86px;top:1907px;width:192px;height:1px;background:#ddd"></div>
  <div class="abs perk" style="top:1932px"><i><svg width="26" height="26" viewBox="0 0 26 26"><circle cx="13" cy="13" r="11" fill="none" stroke="#e0261e" stroke-width="1.5"/><text x="13" y="18" text-anchor="middle" font-size="13" fill="#e0261e" font-family="Montserrat,sans-serif" font-weight="700">$</text></svg></i><div><b>MONEY GUARANTEE</b><p>30 days money back guarantee</p></div></div>
  <div class="abs" style="left:86px;top:1981px;width:192px;height:1px;background:#ddd"></div>
  <div class="abs perk" style="top:2005px"><i><svg width="26" height="26" viewBox="0 0 26 26"><circle cx="9" cy="10" r="6" fill="none" stroke="#e0261e" stroke-width="2.5" stroke-dasharray="3 2"/><circle cx="18" cy="18" r="5" fill="none" stroke="#e0261e" stroke-width="2.5" stroke-dasharray="3 2"/></svg></i><div><b>ONLINE SUPPORT</b><p>We support online 24/24 on day</p></div></div>

  <section class="abs rating" aria-label="Ratewharf reviews">
    <p class="mont" style="margin-top:16px;font-size:22px;color:#333;font-weight:500;display:flex;align-items:center;justify-content:center;gap:6px"><span style="width:16px;height:16px;background:var(--gold);display:inline-block"></span>RATEWHARF</p>
    <div style="display:flex;gap:4px;justify-content:center;margin-top:8px">
      <span style="width:17px;height:17px;background:#3aa14a"></span><span style="width:17px;height:17px;background:#3aa14a"></span><span style="width:17px;height:17px;background:#3aa14a"></span><span style="width:17px;height:17px;background:#3aa14a"></span><span style="width:17px;height:17px;background:#3aa14a"></span>
    </div>
    <p style="margin-top:12px;font-size:21px;color:#444;font-weight:500">Excellent <b class="mont" style="color:#1d2380">9.2/10</b></p>
    <div class="abs" style="left:0;top:117px;width:224px;height:88px;background:#eeeeee">
      <p style="margin-top:14px;font-size:12px;line-height:16px;color:#666;font-weight:600"><b style="color:#333">8,074 Customers</b> Have<br>Reviewed <b style="color:#333">QUENTHOR</b> on Ratewharf</p>
      <span style="display:inline-flex;margin-top:8px;width:101px;height:22px;background:#f0a030;color:#fff;font-size:11px;font-weight:600;align-items:center;justify-content:center">Read Reviews</span>
    </div>
  </section>

  <h2 class="abs sec-title" style="left:339px;top:667px"><svg width="22" height="12" viewBox="0 0 22 12"><path d="M4 0h3L3 12H0zM10 0h3L9 12H6zM16 0h3l-4 12h-3z" fill="#e0261e"/></svg>FEATURED PRODUCTS</h2>
  <p class="abs sec-count" style="left:982px;top:673px">28 Items | <span>View all</span></p>

  <article class="abs product-card" style="left:339px;top:700px"><div class="product-shot" role="img" aria-label="QTP110 injector puller"></div><h3 class="product-name">QTP110</h3><p class="product-desc">Verstuiver-trekker<br>Maravel</p><a class="btn-view">View More</a></article>
  <article class="abs product-card" style="left:532px;top:700px"><div class="product-shot shot-slim" role="img" aria-label="QTP220 TPL injector puller"></div><h3 class="product-name" style="margin-top:12px">QTP220 TPL</h3><p class="product-desc">Verstuiver-trekker<br>1,9 dCi Rovanne,<br>Niskar, Orvel</p><a class="btn-view">View More</a></article>
  <article class="abs product-card" style="left:724px;top:700px"><div class="product-shot shot-case" role="img" aria-label="QTP440 TPL tool case"></div><h3 class="product-name" style="margin-top:14px">QTP440 TPL</h3><p class="product-desc" style="font-size:10px;line-height:14px">Verstuiver-trekker2,0/2,2 HDI 16 valve Pavant, Fenza, Lorvia, Sukama, Ridge Rambler, Valdo, Mikashi, Cirano</p><a class="btn-view">View More</a></article>
  <article class="abs product-card" style="left:917px;top:700px"><div class="product-shot shot-bottle" role="img" aria-label="QLX80 lubricant bottle" style="width:60px"></div><h3 class="product-name" style="margin-top:22px">QLX80</h3><p class="product-desc">Universeel</p><a class="btn-view">View More</a></article>
  <span class="abs arrow" style="left:324px;top:850px"><svg width="8" height="10"><path d="M6 1 2 5l4 4" fill="none" stroke="#333" stroke-width="1.5"/></svg></span>
  <span class="abs arrow" style="left:1072px;top:850px"><svg width="8" height="10"><path d="M2 1l4 4-4 4" fill="none" stroke="#333" stroke-width="1.5"/></svg></span>

  <div class="abs" style="left:351px;top:1039px;width:723px;height:83px;background:linear-gradient(90deg,#6b6b6b,#2b3a4a 50%,#8a3a2a)" role="img" aria-label="Mechanic working under a car"></div>
  <div class="abs" style="left:351px;top:1039px;width:360px;height:83px;background:var(--red);clip-path:polygon(0 0,100% 0,85% 100%,0 100%)"></div>
  <svg class="abs" style="left:370px;top:1056px" width="46" height="46" viewBox="0 0 46 46"><path d="M8 22 22 8h14v14L22 36z" fill="none" stroke="#fff" stroke-width="2.5"/><circle cx="30" cy="14" r="2.5" fill="#fff"/></svg>
  <p class="abs" style="left:435px;top:1055px;font-size:21px;line-height:26px;color:#fff;font-weight:500">Get <span style="color:#f5b23a">10%</span> DISCOUNT on<br>orders over $500</p>

  <h2 class="abs sec-title" style="left:339px;top:1152px"><svg width="22" height="12" viewBox="0 0 22 12"><path d="M4 0h3L3 12H0zM10 0h3L9 12H6zM16 0h3l-4 12h-3z" fill="#e0261e"/></svg>SHOP BY CATEGORIES</h2>
  <p class="abs sec-count" style="left:983px;top:1158px">12 Items | <span>View all</span></p>

  <article class="abs product-card" style="left:339px;top:1184px"><div class="product-shot" role="img" aria-label="QTP110 injector puller"></div><h3 class="product-name">QTP110</h3><p class="product-desc">Verstuiver-trekker<br>Maravel</p><a class="btn-view">View More</a></article>
  <article class="abs product-card" style="left:532px;top:1184px"><div class="product-shot shot-slim" role="img" aria-label="QTP220 TPL injector puller"></div><h3 class="product-name" style="margin-top:12px">QTP220 TPL</h3><p class="product-desc">Verstuiver-trekker<br>1,9 dCi Rovanne,<br>Niskar, Orvel</p><a class="btn-view">View More</a></article>
  <article class="abs product-card" style="left:724px;top:1184px"><div class="product-shot shot-case" role="img" aria-label="QTP440 TPL tool case"></div><h3 class="product-name" style="margin-top:14px">QTP440 TPL</h3><p class="product-desc" style="font-size:10px;line-height:14px">Verstuiver-trekker2,0/2,2 HDI 16 valve Pavant, Fenza, Lorvia, Sukama, Ridge Rambler, Valdo, Mikashi, Cirano</p><a class="btn-view">View More</a></article>
  <article class="abs product-card" style="left:917px;top:1184px"><div class="product-shot shot-bottle" role="img" aria-label="QLX80 lubricant bottle" style="width:60px"></div><h3 class="product-name" style="margin-top:22px">QLX80</h3><p class="product-desc">Universeel</p><a class="btn-view">View More</a></article>
  <span class="abs arrow" style="left:324px;top:1334px"><svg width="8" height="10"><path d="M6 1 2 5l4 4" fill="none" stroke="#333" stroke-width="1.5"/></svg></span>
  <span class="abs arrow" style="left:1072px;top:1334px"><svg width="8" height="10"><path d="M2 1l4 4-4 4" fill="none" stroke="#333" stroke-width="1.5"/></svg></span>

  <h2 class="abs sec-title" style="left:339px;top:1530px;text-transform:none"><svg width="22" height="12" viewBox="0 0 22 12"><path d="M4 0h3L3 12H0zM10 0h3L9 12H6zM16 0h3l-4 12h-3z" fill="#e0261e"/></svg>Last Viewed Products</h2>
  <article class="abs mini-card current" style="left:387px"><h4>QTP110</h4><div class="mini-shot" role="img" aria-label="QTP110 injector puller"></div><a class="btn-view">View More</a></article>
  <article class="abs mini-card" style="left:557px"><h4>QTP440 TPL</h4><div class="mini-shot" role="img" aria-label="QTP440 TPL tool case" style="width:70px;height:70px;margin-top:18px"></div><a class="btn-view">View More</a></article>
  <article class="abs mini-card" style="left:732px"><h4>QTP110</h4><div class="mini-shot" role="img" aria-label="QTP220 injector puller" style="background:linear-gradient(180deg,#d8c23a,#8c8c8c 60%,#bdbdbd)"></div><a class="btn-view">View More</a></article>
  <article class="abs mini-card" style="left:898px"><h4>QTP110</h4><div class="mini-shot" role="img" aria-label="QTP110 injector puller"></div><a class="btn-view">View More</a></article>
  <svg class="abs" style="left:352px;top:1647px" width="10" height="14"><path d="M8 1 2 7l6 6" fill="none" stroke="#333" stroke-width="1.6"/></svg>
  <svg class="abs" style="left:1072px;top:1647px" width="10" height="14"><path d="M2 1l6 6-6 6" fill="none" stroke="#333" stroke-width="1.6"/></svg>

  <h2 class="abs sec-title" style="left:353px;top:1794px"><svg width="22" height="12" viewBox="0 0 22 12"><path d="M4 0h3L3 12H0zM10 0h3L9 12H6zM16 0h3l-4 12h-3z" fill="#e0261e"/></svg>QUENTHOR Benefits</h2>
  <div class="abs benefit-icon" style="top:1838px;font-style:italic">TM</div>
  <p class="abs benefit-title" style="top:1849px">MANY FAMOUS BRANDS</p>
  <p class="abs benefit-text" style="top:1866px">At Quenthor you will find more than 2000 articles from various brands. Also from very famous brands.</p>
  <div class="abs benefit-icon" style="top:1937px"><svg width="26" height="22" viewBox="0 0 26 22"><rect x="1" y="1" width="24" height="20" fill="none" stroke="#d1d1d1" stroke-width="1.5"/><path d="M5 7h8M5 11h16M5 15h16" stroke="#d1d1d1" stroke-width="1.5"/></svg></div>
  <p class="abs benefit-title" style="top:1948px">LOTS OF ARTICLES&gt; 2000</p>
  <p class="abs benefit-text" style="top:1965px">Quenthor is constantly working to keep the range of items up to date and to be able to offer you as a customer the best.</p>
  <div class="abs benefit-icon" style="top:2042px;font-size:12px">100%</div>
  <p class="abs benefit-title" style="top:2057px">100% GUARANTEE</p>
  <p class="abs benefit-text" style="top:2073px">Our prices may be quite low, but this must not be at the expense of quality. That is why the Quenthor offers you a 100% guarantee on all our items.</p>
  <div class="abs" role="img" aria-label="Laptop showing the webshop" style="left:832px;top:1876px;width:248px;height:165px;background:linear-gradient(135deg,#1c2a66,#c84040 45%,#e8c24a 70%,#2a2a2a);border:8px solid #1a1a1a;border-radius:8px 8px 0 0"></div>
  <div class="abs" style="left:802px;top:2041px;width:304px;height:10px;background:#b8b8b8;border-radius:0 0 10px 10px"></div>

  <div class="abs brand-cell" style="left:344px;width:152px">FERVANI</div>
  <div class="abs brand-cell" style="left:499px;width:160px;color:#999;font-weight:400;letter-spacing:4px">LYRENT</div>
  <div class="abs brand-cell" style="left:661px;width:161px;color:#1d3a8a">ARDENA</div>
  <div class="abs brand-cell" style="left:824px;width:160px;font-size:13px">KORVAN</div>
  <div class="abs brand-cell" style="left:987px;width:159px;font-size:14px;font-weight:500;letter-spacing:3px">BELCREST</div>
  <span class="abs arrow" style="left:324px;top:2197px"><svg width="8" height="10"><path d="M6 1 2 5l4 4" fill="none" stroke="#333" stroke-width="1.5"/></svg></span>
  <span class="abs arrow" style="left:1134px;top:2197px"><svg width="8" height="10"><path d="M2 1l4 4-4 4" fill="none" stroke="#333" stroke-width="1.5"/></svg></span>

  <section class="abs news" aria-label="Newsletter"></section>
  <a class="abs sq" style="left:60px" aria-label="Social channel 1"></a>
  <a class="abs sq" style="left:105px" aria-label="Social channel 2"></a>
  <a class="abs sq" style="left:150px" aria-label="Social channel 3"></a>
  <a class="abs sq" style="left:195px" aria-label="Social channel 4"></a>
  <a class="abs sq" style="left:240px" aria-label="Social channel 5"></a>
  <a class="abs sq" style="left:285px" aria-label="Social channel 6"></a>
  <p class="abs mont" style="left:430px;top:2339px;width:390px;font-size:14px;line-height:16px;color:#e8e8e8;font-weight:700">SIGN UP FOR NEWSLETTER &amp; GET 20% OFF ON FIRST ORDER</p>
  <div class="abs" style="left:824px;top:2329px;width:227px;height:36px;background:#fff;font-size:11px;color:#555;display:flex;align-items:center;padding-left:12px;font-weight:600">Your email address...</div>
  <a class="abs" style="left:1051px;top:2329px;width:95px;height:36px;background:var(--red);color:#fff;font-size:11px;font-weight:700;display:flex;align-items:center;justify-content:center">SUBSCRIBE</a>

  <footer class="abs footer"></footer>

  <svg class="abs" style="left:100px;top:2430px" width="44" height="34" viewBox="0 0 44 34"><rect x="2" y="8" width="24" height="18" fill="#8bbb3b"/><path d="M26 13h9l6 7v6H26z" fill="#e2b52b"/><circle cx="10" cy="28" r="4" fill="#555"/><circle cx="34" cy="28" r="4" fill="#555"/></svg>
  <p class="abs feat-title" style="left:152px;top:2426px">Assured Purchase</p>
  <p class="abs feat-sub" style="left:152px;top:2452px">Provide genuine service &amp; store products</p>
  <ul class="abs ticks" style="left:152px;top:2490px"><li>100% genuine products</li><li>Deliver items at door</li><li>Free to return products</li></ul>

  <svg class="abs" style="left:366px;top:2432px" width="44" height="30" viewBox="0 0 44 30"><rect x="1" y="3" width="34" height="22" rx="2" fill="#5aa048"/><circle cx="18" cy="14" r="6" fill="#a6d08a"/><rect x="30" y="14" width="12" height="12" fill="#e2b52b"/></svg>
  <p class="abs feat-title" style="left:419px;top:2426px">Esay To Buy &amp; Return</p>
  <p class="abs feat-sub" style="left:419px;top:2452px">Single click to buy &amp; return products</p>
  <ul class="abs ticks" style="left:419px;top:2490px"><li>Same day devilery available</li><li>Click to return products</li><li>Quick support links available</li></ul>

  <svg class="abs" style="left:640px;top:2428px" width="32" height="40" viewBox="0 0 32 40"><circle cx="16" cy="15" r="13" fill="#e2a02b"/><circle cx="16" cy="15" r="8" fill="#f5c65a"/><path d="M9 26 6 39l10-5 10 5-3-13" fill="#d04a2a"/></svg>
  <p class="abs feat-title" style="left:685px;top:2426px">Secure Payments</p>
  <p class="abs feat-sub" style="left:685px;top:2452px">Accepts all credit &amp; debit cards</p>
  <ul class="abs ticks" style="left:685px;top:2474px"><li>100% payment security</li><li>Confirmation authentity</li><li>delivery items at door</li></ul>

  <svg class="abs" style="left:906px;top:2428px" width="30" height="38" viewBox="0 0 30 38"><rect x="2" y="2" width="26" height="34" fill="#f2f2f2"/><rect x="2" y="2" width="26" height="8" fill="#d04a2a"/><path d="M7 16h16M7 21h16M7 26h10" stroke="#999" stroke-width="1.5"/></svg>
  <p class="abs feat-title" style="left:952px;top:2426px">Download Center</p>
  <p class="abs" style="left:957px;top:2449px;font-size:11px;line-height:14px;color:#bbb;font-weight:600"><u style="color:var(--red)">Click here</u> to<br>Download Catalog</p>

  <a class="abs brand" style="left:95px;top:2609px;gap:8px"><span class="brand-square" style="width:26px;height:26px"></span><span class="brand-name" style="font-size:19px">QUENTHOR</span></a>
  <p class="abs foot-text" style="left:95px;top:2652px;width:205px">Quenthor BV is a company that specializes in the development and production of special dismantling tools for the automotive industry. The tool is especially suitable for removing glow plugs and injectors by means of vibrations.</p>

  <p class="abs foot-h" style="left:360px;top:2614px">Useful Links</p>
  <ul class="abs foot-links" style="left:360px;top:2647px"><li>frequently asked questions</li><li>privacy</li><li>returns and warranty</li><li>terms and conditions</li><li>shipping</li></ul>

  <p class="abs foot-h" style="left:576px;top:2614px">Contact us</p>
  <p class="abs foot-text" style="left:576px;top:2640px;line-height:15px"><span style="color:#c8c8c8;font-size:13px">Correspondentieadres</span><br>Quenthor B.V.<br>Postbus 512<br>2900 KR ALMENDAAL</p>
  <p class="abs foot-text" style="left:754px;top:2640px;line-height:15px"><span style="color:#c8c8c8;font-size:13px">Service/Productie:</span><br>Vlasstraat 27b<br>2901 BL Almendaal<br>Nederland</p>
  <p class="abs foot-text" style="left:576px;top:2716px;line-height:17px">Tel: 010-4400182 &nbsp;&nbsp;&nbsp;Fax: 010-4400189<br>info@quenthor.nl<br><span style="color:#c8c8c8;font-size:11px">Chamber of Commerce 58213374</span><br><span style="color:#c8c8c8;font-size:11px">VAT NL851204337B01</span></p>

  <p class="abs foot-h" style="left:891px;top:2614px">Useful Videos</p>
  <div class="abs" style="left:890px;top:2644px;width:245px;height:133px;background:#1e1e1e"></div>
  <div class="abs" role="img" aria-label="Company video thumbnail" style="left:925px;top:2644px;width:163px;height:133px;background:linear-gradient(180deg,#eef0f8,#c9ccda)">
    <svg class="abs" style="left:62px;top:40px" width="40" height="40" viewBox="0 0 40 40"><circle cx="20" cy="20" r="18" fill="#fff" stroke="#555" stroke-width="2"/><path d="M16 12v16l12-8z" fill="#555"/></svg>
  </div>
  <svg class="abs" style="left:900px;top:2704px" width="8" height="12"><path d="M7 1 2 6l5 5" fill="none" stroke="#aaa" stroke-width="1.5"/></svg>
  <svg class="abs" style="left:1116px;top:2704px" width="8" height="12"><path d="M1 1l5 5-5 5" fill="none" stroke="#aaa" stroke-width="1.5"/></svg>

  <p class="abs" style="left:0;width:1230px;top:2828px;text-align:center;font-size:12.5px;color:#bbb;font-weight:600">Accepted Payment Methods</p>
  <span class="abs pay" style="left:453px;background:#d33" aria-label="Payment method"></span>
  <span class="abs pay" style="left:494px;background:#2a6fb8" aria-label="Payment method"></span>
  <span class="abs pay" style="left:535px;background:#ddd" aria-label="Payment method"></span>
  <span class="abs pay" style="left:576px;background:#f2f2f2" aria-label="Payment method"></span>
  <span class="abs pay" style="left:617px;background:#3a4fb0" aria-label="Payment method"></span>
  <span class="abs pay" style="left:658px;background:#e06a3a" aria-label="Payment method"></span>
  <span class="abs pay" style="left:699px;background:#2a3a8a" aria-label="Payment method"></span>
  <span class="abs pay" style="left:740px;background:#f4f4f4" aria-label="Payment method"></span>

  <div class="abs copyright">Copyright © All Right Reserved QUENTHOR &nbsp;2020</div>
  <div class="abs cookie">This website uses cookies to measure the visit, we do not store any personal data.<span style="font-size:8px">Disable cookies</span><span class="cookie-btn">Accept cookies</span></div>

</div>
</body>
</html>
```